Website for Vayu Kiran Holdings

Need a project marketing website for our company which primarily deals in selling real estate(land sales) from Big Estates to Builders /Clients, help them in Building & Construction and do all Project Management.

Coding

Coded - Design and coding required

Number of Pages Required

4 page

Colors
0054AA
0677BA
7BADD7
CADEEF
E8F1F8
FFC000
F8CF3A
FAE287
FDF2CF
FEFAEE

```html
<!DOCTYPE html>
<html lang="en">
<head>
<meta charset="UTF-8">
<title>Investments – Vayu Kiran Holdings</title>
<link rel="stylesheet" href="https://fonts.googleapis.com/css2?family=Montserrat:wght@400;500;600&family=Playfair+Display:wght@400&family=Poppins:wght@700&display=swap">
<style>
  :root {
    --blue-deep: #0054AA;
    --blue: #0677BA;
    --blue-soft: #7BADD7;
    --blue-pale: #CADEEF;
    --yellow: #FFC000;
    --ink: #1d1f24;
    --footer: #2c333d;
    --footer-line: #414954;
    --white: #ffffff;
  }
  * { box-sizing: border-box; margin: 0; padding: 0; }
  html, body { width: 956px; height: 1200px; overflow: hidden; }
  body {
    position: relative;
    background: var(--white);
    font-family: "Montserrat", sans-serif;
    color: var(--ink);
  }
  .abs { position: absolute; }

  /* Hero */
  .hero {
    left: 0; top: 0; width: 956px; height: 433px;
    background:
      radial-gradient(ellipse 200px 170px at 640px 200px, rgba(6,119,186,.75), rgba(6,119,186,0) 75%),
      linear-gradient(90deg, #e6e6e6 0%, #dcdcdc 40%, #4a4a4a 62%, #2b2b2b 72%, #8a8a8a 100%);
  }
  .hero-shade {
    left: 0; top: 300px; width: 956px; height: 133px;
    background: linear-gradient(180deg, rgba(150,150,150,0), rgba(120,120,120,.45));
  }
  .brand {
    left: 112px; top: 20px;
    font-weight: 600; font-size: 20px; color: var(--blue-deep);
    display: flex; align-items: center; gap: 8px;
  }
  .brand .mark { width: 24px; height: 24px; background: var(--blue-deep); }
  .nav { left: 573px; top: 30px; display: flex; gap: 35px; font-size: 9.5px; color: var(--white); }
  .btn-start {
    left: 776px; top: 26px; width: 68px; height: 21px;
    background: var(--blue-deep); color: var(--white);
    font-size: 9.5px; display: flex; align-items: center; justify-content: center; border-radius: 1px;
  }
  .header-rule { left: 112px; top: 75px; width: 732px; height: 1px; background: rgba(255,255,255,.55); }
  .hero-title {
    left: 112px; top: 197px; width: 264px; height: 91px;
    background: var(--blue-soft);
    clip-path: polygon(0 0, 100% 0, 84.5% 100%, 0 100%);
  }
  .hero-title h1 {
    position: absolute; left: 26px; top: 26px;
    font-family: "Poppins", sans-serif; font-weight: 700; font-size: 29px; color: var(--white); line-height: 1.2;
  }

  /* Breadcrumb */
  .crumbs { left: 114px; top: 447px; font-size: 9.5px; display: flex; gap: 10px; color: #333; }
  .crumbs strong { font-weight: 600; }

  /* Intro */
  .intro-photo {
    left: 141px; top: 516px; width: 278px; height: 281px;
    background: linear-gradient(135deg, #8b8f94 0%, #5c6066 45%, #2f3135 100%);
  }
  .intro-cut { left: 141px; top: 504px; width: 292px; height: 293px; }
  .intro-text { left: 522px; top: 522px; width: 318px; }
  .intro-text h2 {
    font-family: "Playfair Display", serif; font-weight: 400; font-size: 26px; color: var(--blue-deep); line-height: 1.2;
    margin-bottom: 12px;
  }
  .intro-text p { font-size: 10px; line-height: 18.4px; margin-bottom: 6px; }
  .btn-contact {
    left: 522px; top: 742px; width: 101px; height: 27px;
    background: var(--yellow); border-radius: 14px;
    font-size: 10.5px; font-weight: 600; color: var(--ink);
    display: flex; align-items: center; padding-left: 12px;
  }
  .btn-contact .arrow {
    position: absolute; right: 2px; top: 2px; width: 23px; height: 23px; border-radius: 50%;
    background: var(--blue-deep);
  }

  /* Footer */
  .footer-shape { left: 0; top: 800px; width: 956px; height: 400px; }
  .f-brand {
    left: 112px; top: 1004px; width: 160px; font-weight: 600; font-size: 17px; line-height: 1.1; color: var(--white);
    display: flex; align-items: center; gap: 8px;
  }
  .f-brand .mark { flex: none; width: 22px; height: 22px; background: var(--white); }
  .f-rule { left: 112px; top: 1059px; width: 155px; height: 1px; background: var(--footer-line); }
  .social { left: 135px; top: 1073px; display: flex; gap: 6px; }
  .social span { width: 22px; height: 22px; border-radius: 50%; background: var(--yellow); display: block; }
  .f-col h3 {
    font-family: "Playfair Display", serif; font-weight: 400; font-size: 15px; color: var(--white); margin-bottom: 14px;
  }
  .f-col { color: #e4e7eb; font-size: 9.5px; }
  .links li { list-style: none; display: flex; align-items: center; gap: 6px; height: 19px; }
  .links li::before {
    content: ""; width: 5px; height: 5px; border: 1.5px solid var(--blue); border-radius: 50%; background: transparent;
  }
  .contact-item { display: flex; gap: 8px; line-height: 13.5px; margin-bottom: 8px; }
  .contact-item svg { flex: none; width: 12px; height: 12px; margin-top: 1px; }
  .newsletter p { line-height: 13.5px; margin-bottom: 15px; }
  .newsletter .field {
    width: 197px; height: 28px; background: var(--white); color: #444;
    font-size: 9px; display: flex; align-items: center; padding-left: 9px;
  }
  .bottom-rule { left: 0; top: 1142px; width: 956px; height: 1px; background: var(--footer-line); }
  .copyright { left: 0; top: 1165px; width: 956px; text-align: center; font-size: 9.5px; color: #e4e7eb; }
</style>
</head>
<body>

  <section class="abs hero" role="img" aria-label="Businessman holding a glowing house over a blue city skyline"></section>
  <div class="abs hero-shade"></div>

  <header>
    <div class="abs brand"><span class="mark"></span>Vayu Kiran Holdings</div>
    <nav class="abs nav"><span>Home</span><span>Services</span><span>Contact</span></nav>
    <div class="abs btn-start">Get Started</div>
    <div class="abs header-rule"></div>
  </header>

  <div class="abs hero-title"><h1>Investments</h1></div>

  <div class="abs crumbs"><span>Home</span><span>/</span><strong>Investments</strong></div>

  <div class="abs intro-photo" role="img" aria-label="Advisor signing documents beside a model building"></div>
  <svg class="abs intro-cut" viewBox="0 0 292 293" aria-hidden="true">
    <line x1="0" y1="0" x2="292" y2="293" stroke="#fff" stroke-width="14"/>
  </svg>

  <div class="abs intro-text">
    <h2>Investments</h2>
    <p>At Vayu Kiran Holdings, we identify and manage high-value investment opportunities across diverse sectors.</p>
    <p>Our approach is rooted in careful analysis, market research, and a deep understanding of financial trends. We work closely with our clients to develop tailored investment strategies that align with their goals-whether that means steady growth, wealth preservation, or long-term capital appreciation.</p>
  </div>

  <div class="abs btn-contact">Contact Us
    <span class="arrow">
      <svg viewBox="0 0 23 23" width="23" height="23"><path d="M6 11.5h10M12 7.5l4 4-4 4" fill="none" stroke="#fff" stroke-width="2" stroke-linecap="round" stroke-linejoin="round"/></svg>
    </span>
  </div>

  <footer>
    <svg class="abs footer-shape" viewBox="0 0 956 400" preserveAspectRatio="none" aria-hidden="true">
      <polygon points="956,4 956,400 0,400 0,153" fill="#2c333d"/>
      <polygon points="0,48 292,107 0,153" fill="#FFC000"/>
    </svg>

    <div class="abs f-brand"><span class="mark"></span><span>Vayu Kiran<br>Holdings</span></div>
    <div class="abs f-rule"></div>
    <div class="abs social" aria-label="Social links"><span></span><span></span><span></span><span></span></div>

    <div class="abs f-col" style="left:303px; top:993px;">
      <h3>Quick Links</h3>
      <ul class="links"><li>Home</li><li>Services</li><li>Contact Us</li></ul>
    </div>

    <div class="abs f-col" style="left:433px; top:993px;">
      <h3>Contact Details</h3>
      <div class="contact-item">
        <svg viewBox="0 0 12 12"><path d="M6 1a3.5 3.5 0 0 0-3.5 3.5C2.5 7 6 11 6 11s3.5-4 3.5-6.5A3.5 3.5 0 0 0 6 1z" fill="#fff"/><circle cx="6" cy="4.5" r="1.3" fill="#2c333d"/></svg>
        <span>48/3 Meridian Way Laverton<br>VIC 3028</span>
      </div>
      <div class="contact-item">
        <svg viewBox="0 0 12 12"><path d="M2.5 1.5l2 .3.7 2.2-1.2 1a7 7 0 0 0 3 3l1-1.2 2.2.7.3 2c-4.5.5-8.5-3.5-8-8z" fill="#fff"/></svg>
        <span>0400123987</span>
      </div>
      <div class="contact-item">
        <svg viewBox="0 0 12 12"><rect x="1" y="2.5" width="10" height="7" rx="1" fill="#fff"/><path d="M1.5 3l4.5 3.5L10.5 3" fill="none" stroke="#2c333d" stroke-width="1"/></svg>
        <span>info@vayukiranholdings.com.au</span>
      </div>
    </div>

    <div class="abs f-col newsletter" style="left:647px; top:993px;">
      <h3>Newsletter Sign Up</h3>
      <p>Subscribe to our newsletter to get the<br>latest update to your inbox</p>
      <div class="field">Email address</div>
    </div>

    <div class="abs bottom-rule"></div>
    <div class="abs copyright">© 2025 Vayu Kiran Holdings. All Rights Reserved.</div>
  </footer>

</body>
</html>
```